Retractable Banner Design for Youth Group

I would like the signage with the following as well as the following:
YOUTH VISION: Realigning the blueprint of our youth to God’s original plan.
YOUTH MISSION: Developing a generation of young people who are confident of God's irrefutable love; healing power; mercy and forgiveness; and, sovereignty.

The banner size is 33.5x 79 inches

Target Market(s)

Teenagers

Industry/Entity Type

Religious

Colors

Designer to choose colors to be used in the design.

Requirements
Must have
• Logo
• Inner Healing
• Discipleship
• Leadership Development

```html
<!DOCTYPE html>
<html lang="en">
<head>
<meta charset="utf-8">
<title>Brightpath Youth – Retractable Banner</title>
<link href="https://fonts.googleapis.com/css2?family=Cinzel:wght@400;600&family=Roboto:ital,wght@0,400;1,700&display=swap" rel="stylesheet">
<style>
  :root {
    --stage: #e6e8ea;
    --white: #ffffff;
    --brand-red: #9b1c22;
    --ink-grey: #555a66;
    --royal: #2b3686;
    --sky: #4a7fd0;
    --sky-light: #cfe1f6;
    --pill: rgba(60, 80, 160, 0.75);
  }
  html, body {
    margin: 0;
    width: 1200px;
    height: 1200px;
    overflow: hidden;
    background: var(--stage);
  }
  .canvas {
    position: relative;
    width: 1200px;
    height: 1200px;
  }
  .banner {
    position: absolute;
    left: 358px;
    top: 30px;
    width: 484px;
    height: 1140px;
    overflow: hidden;
    background: linear-gradient(180deg,
      var(--white) 0%,
      var(--white) 20%,
      var(--sky-light) 34%,
      var(--sky) 50%,
      #3550a8 62%,
      var(--royal) 72%,
      var(--royal) 100%);
    color: var(--white);
    font-family: "Roboto", sans-serif;
    text-align: center;
  }
  .brand {
    position: absolute;
    top: 120px;
    left: 0;
    width: 100%;
  }
  .brand-mark {
    display: block;
    width: 56px;
    height: 56px;
    margin: 0 auto 14px;
    border-radius: 50%;
    background: var(--brand-red);
  }
  .brand-name {
    margin: 0;
    font-family: "Roboto", sans-serif;
    font-weight: 400;
    font-size: 32px;
    line-height: 38px;
    color: var(--brand-red);
  }
  .brand-tagline {
    margin: 4px 0 0;
    font-family: "Roboto", sans-serif;
    font-size: 12px;
    line-height: 16px;
    letter-spacing: 1px;
    color: var(--ink-grey);
  }
  .sky-photo {
    position: absolute;
    top: 215px;
    left: 0;
    width: 100%;
    height: 420px;
    background:
      radial-gradient(ellipse 60% 45% at 50% 25%, rgba(255,255,255,0.95), rgba(255,255,255,0) 70%),
      radial-gradient(ellipse 80% 30% at 50% 75%, rgba(255,255,255,0.55), rgba(255,255,255,0) 70%);
  }
  .icon {
    position: absolute;
    left: 50%;
    transform: translateX(-50%);
  }
  .icon-eye { top: 470px; }
  .icon-target { top: 690px; }
  .pill {
    position: absolute;
    left: 50%;
    transform: translateX(-50%);
    padding: 0 22px;
    height: 37px;
    border-radius: 10px;
    background: var(--pill);
    font-family: "Cinzel", serif;
    font-weight: 400;
    font-size: 30px;
    line-height: 38px;
    letter-spacing: 1px;
    white-space: nowrap;
  }
  .pill-vision { top: 560px; }
  .pill-mission { top: 810px; }
  .statement {
    position: absolute;
    left: 0;
    width: 100%;
    margin: 0;
    font-size: 24px;
    line-height: 30px;
  }
  .statement-vision { top: 609px; }
  .statement-mission { top: 862px; }
  .footer {
    position: absolute;
    left: 0;
    bottom: 0;
    width: 100%;
    height: 96px;
    background: var(--brand-red);
    border-top: 2px solid var(--white);
    box-shadow: 0 -3px 0 var(--royal);
  }
  .website {
    margin: 0;
    font-style: italic;
    font-weight: 700;
    font-size: 35px;
    line-height: 84px;
    color: var(--white);
  }
</style>
</head>
<body>
<main class="canvas">
  <section class="banner">
    <header class="brand">
      <span class="brand-mark"></span>
      <h1 class="brand-name">Brightpath Youth</h1>
      <p class="brand-tagline">GROW . SERVE . LEAD</p>
    </header>

    <div class="sky-photo" role="img" aria-label="White dove with spread wings descending through bright light rays over blue sky and clouds"></div>

    <svg class="icon icon-eye" width="120" height="82" viewBox="0 0 120 82" aria-hidden="true">
      <path d="M2 42 Q60 -18 118 42 Q60 102 2 42 Z" fill="#7a7f8e"/>
      <path d="M2 38 Q60 -22 118 38 Q60 98 2 38 Z" fill="#2b3686"/>
      <circle cx="60" cy="38" r="28" fill="#ffffff"/>
      <circle cx="60" cy="38" r="22" fill="#2b3686"/>
      <circle cx="52" cy="30" r="7" fill="#ffffff"/>
    </svg>
    <div class="pill pill-vision">YOUTH VISION</div>
    <p class="statement statement-vision">Realigning the blueprint of our youth<br>to God’s original plan.</p>

    <svg class="icon icon-target" width="92" height="92" viewBox="0 0 92 92" aria-hidden="true">
      <g fill="none" stroke="#ffffff" stroke-width="7">
        <circle cx="46" cy="46" r="38"/>
        <circle cx="46" cy="46" r="24"/>
        <circle cx="46" cy="46" r="11"/>
      </g>
      <g stroke="#2b3686" stroke-width="10">
        <line x1="46" y1="0" x2="46" y2="92"/>
        <line x1="0" y1="46" x2="92" y2="46"/>
      </g>
      <g stroke="#ffffff" stroke-width="4">
        <line x1="46" y1="2" x2="46" y2="90"/>
        <line x1="2" y1="46" x2="90" y2="46"/>
      </g>
    </svg>
    <div class="pill pill-mission">YOUTH MISSION</div>
    <p class="statement statement-mission">Developing a generation of young<br>people who are confident of God's<br>irrefutable love; healing power;<br>mercy and forgiveness;<br>and, sovereignty.</p>

    <footer class="footer">
      <p class="website">www.yourwebsite.com</p>
    </footer>
  </section>
</main>
</body>
</html>
```